Dental Business Card

I need Dental oriented business cards.
On the front side -
- on the first line, my name:
Dr Marlo Vintner
- on the second line (just underneath):
Doctor of Dental Medicine
- on the third line, or underneath that or in a corner, I would like the address and phone number:
5182 Ch. Birchfield
Montreal QC H2T 4B9
514-629-5074
- other than that i would maybe like a logo of a tooth, but i want it to be subtle and very basic!
- I would like the card to be preferably black or dark grey-ish with the writing in white
On the other side -
- 2-3 lines with the possibility to write the next appointment the box with the lines should be white, with the rest of the card being black

```html
<!DOCTYPE html>
<html lang="en">
<head>
<meta charset="utf-8">
<title>Dental Business Card – Front and Back</title>
<link rel="stylesheet" href="https://fonts.googleapis.com/css2?family=Montserrat:wght@300;400;700&display=swap">
<style>
  :root {
    --backdrop: #e3e4e8;
    --card-dark: #0b0b0b;
    --card-mid: #181818;
    --text-light: #f1f1f1;
    --teal-deep: #3d8b95;
    --teal-light: #bfe2e6;
    --field-white: #f7f7f7;
  }
  * { margin: 0; padding: 0; box-sizing: border-box; }
  html, body {
    width: 1200px; height: 1200px; overflow: hidden;
    background: var(--backdrop);
    font-family: "Montserrat", Arial, sans-serif;
  }
  .canvas { position: relative; width: 1200px; height: 1200px; }
  .card {
    position: absolute; left: 219px; width: 762px; height: 436px;
    background: linear-gradient(160deg, var(--card-mid) 0%, var(--card-dark) 100%);
    color: var(--text-light);
  }
  .card--front { top: 109px; }
  .card--back { top: 654px; }
  .corner { position: absolute; width: 40px; height: 40px; }
  .corner--tl { left: 35px; top: 27px; }
  .corner--tr { right: 25px; top: 27px; transform: scaleX(-1); }
  .corner--bl { left: 35px; bottom: 25px; transform: scaleY(-1); }
  .corner--br { right: 25px; bottom: 25px; transform: scale(-1, -1); }

  .doctor-name {
    position: absolute; left: 94px; top: 128px;
    font-weight: 700; font-size: 37px; letter-spacing: 0.5px; line-height: 1;
  }
  .doctor-title {
    position: absolute; left: 94px; top: 171px;
    font-weight: 300; font-size: 20px; letter-spacing: 0.6px; line-height: 1;
  }
  .contact {
    position: absolute; left: 95px; top: 325px;
    font-weight: 300; font-size: 16px; letter-spacing: 0.7px; line-height: 20px;
    font-style: normal;
  }
  .practice-mark {
    position: absolute; left: 500px; top: 200px; width: 170px;
    display: flex; align-items: center; gap: 8px; justify-content: center;
    color: var(--teal-deep); font-weight: 400; font-size: 18px; line-height: 1.2;
  }
  .practice-mark__dot { width: 12px; height: 12px; border-radius: 50%; background: var(--teal-deep); flex: none; }

  .appointment-title {
    position: absolute; left: 0; right: 0; top: 88px; text-align: center;
    font-weight: 400; font-size: 37px; letter-spacing: 1px; line-height: 1;
  }
  .appointment-row { position: absolute; left: 84px; right: 75px; height: 41px; display: flex; align-items: center; }
  .appointment-row--name { top: 183px; }
  .appointment-row--date { top: 239px; }
  .appointment-row--time { top: 295px; }
  .appointment-label { width: 98px; font-weight: 300; font-size: 28px; letter-spacing: 0.5px; }
  .appointment-field {
    flex: 1; height: 41px;
    background: linear-gradient(90deg, #ececec 0%, var(--field-white) 100%);
  }
</style>
</head>
<body>
<svg width="0" height="0" style="position:absolute">
  <defs>
    <linearGradient id="corner-teal" x1="0" y1="0" x2="1" y2="1">
      <stop offset="0" stop-color="#3d8b95"/>
      <stop offset="1" stop-color="#5aa3ab"/>
    </linearGradient>
    <linearGradient id="corner-pale" x1="0" y1="0" x2="1" y2="1">
      <stop offset="0" stop-color="#d3ecee"/>
      <stop offset="1" stop-color="#a9d5da"/>
    </linearGradient>
    <symbol id="corner-shape" viewBox="0 0 40 40">
      <polygon points="0,0 39,0 7,6 0,39"/>
    </symbol>
  </defs>
</svg>

<main class="canvas">
  <section class="card card--front" aria-label="Business card front">
    <svg class="corner corner--tl" fill="url(#corner-teal)"><use href="#corner-shape"/></svg>
    <svg class="corner corner--tr" fill="url(#corner-pale)"><use href="#corner-shape"/></svg>
    <svg class="corner corner--bl" fill="url(#corner-teal)"><use href="#corner-shape"/></svg>
    <svg class="corner corner--br" fill="url(#corner-pale)"><use href="#corner-shape"/></svg>

    <h1 class="doctor-name">Dr. Marlo Vintner</h1>
    <p class="doctor-title">Doctor of Dental Medicine</p>
    <address class="contact">
      5182 Ch. Birchfield<br>
      Montreal QC H2T 4B9<br>
      514-629-5074
    </address>

    <div class="practice-mark">
      <span class="practice-mark__dot"></span>
      <span class="practice-mark__name">Birchfield Dental</span>
    </div>
  </section>

  <section class="card card--back" aria-label="Business card back">
    <svg class="corner corner--tl" fill="url(#corner-teal)"><use href="#corner-shape"/></svg>
    <svg class="corner corner--tr" fill="url(#corner-pale)"><use href="#corner-shape"/></svg>
    <svg class="corner corner--bl" fill="url(#corner-teal)"><use href="#corner-shape"/></svg>
    <svg class="corner corner--br" fill="url(#corner-pale)"><use href="#corner-shape"/></svg>

    <h2 class="appointment-title">Appointment</h2>
    <div class="appointment-row appointment-row--name">
      <span class="appointment-label">Name:</span><span class="appointment-field"></span>
    </div>
    <div class="appointment-row appointment-row--date">
      <span class="appointment-label">Date:</span><span class="appointment-field"></span>
    </div>
    <div class="appointment-row appointment-row--time">
      <span class="appointment-label">Time:</span><span class="appointment-field"></span>
    </div>
  </section>
</main>
</body>
</html>
```